Upscale Wine Cooler/Ready to drink Can Design

We need to design the branding and packaging for a new wine cooler that will be sold in a can. We are also looking for the brand name at this point, so you can be as creative as you can!

The product will have 3 flavours (Cavoni Spritz, Ginger-Lime Spritz, Raspeberry-Mimosa) and will be made of genuine high quality European Wine, with natural flavours

Can dimensions : Height 157 mm ; Diameter : 58 mm
Updates

Need extra days to review

Target Market(s)

Females 19 to 35, who are looking for an alternative to the traditional alcoholic beverages, and who want to drink an upscale and "classy" beverage

Colors

Designer to choose colors to be used in the design.

Requirements
Must have
• Modern, attractive and upscale look
• Brand name
• 3 different cans for each of the flavours : Cavoni Spritz, Ginger-Lime Spritz, Raspeberry-Mimosa
• 355 ml
• 5% alc./vol.

```html
<!DOCTYPE html>
<html lang="en">
<head>
<meta charset="utf-8">
<title>Velluta – Wine Spritz Can Range</title>
<link rel="stylesheet" href="https://fonts.googleapis.com/css2?family=Saira:wght@500;700&family=Oswald:wght@700&family=Michroma&family=Montserrat:wght@700&family=Pinyon+Script&display=swap">
<style>
  :root{
    --stage:#0c0c0c;
    --cap-dark:#1e1e1e;
    --cap-mid:#3a3a3a;
    --body-light:#f4f4f4;
    --body-shade:#d9d9d9;
    --ink:#1b1b1b;
    --orange:#f0821a;
    --orange-band:#f2b233;
    --gold:#e9b43a;
    --green:#2aa35e;
    --green-band:#3cbf78;
    --green-deep:#1d5a33;
    --silver:#dcdcdc;
    --red:#d3203a;
    --red-band:#e02b43;
    --maroon:#5a1322;
  }
  *{margin:0;padding:0;box-sizing:border-box}
  html,body{width:1200px;height:1200px;overflow:hidden;background:var(--stage)}
  .range{position:relative;width:1200px;height:1200px}
  .label{
    position:absolute;top:290px;width:300px;height:640px;overflow:hidden;border-radius:6px;
    background:linear-gradient(90deg,var(--body-shade) 0%,var(--body-light) 30%,#fff 55%,var(--body-light) 75%,var(--body-shade) 100%);
  }
  .label--cavoni{left:50px}
  .label--ginger{left:450px}
  .label--raspberry{left:850px}
  .label__cap{
    position:absolute;left:0;top:0;width:100%;height:150px;
    background:linear-gradient(90deg,var(--cap-dark),var(--cap-mid) 45%,var(--cap-dark));
  }
  .brand{
    position:absolute;left:40px;top:82px;width:220px;height:112px;border-radius:14px;
    background:#222;border:2px solid #555;
    display:flex;align-items:center;justify-content:center;
    font-family:"Saira",sans-serif;font-weight:700;font-size:42px;letter-spacing:1px;
  }
  .label--cavoni .brand{color:var(--gold)}
  .label--ginger .brand{color:var(--silver)}
  .label--raspberry .brand{color:var(--red)}
  .quality-band{
    position:absolute;left:0;top:258px;width:100%;height:24px;
    font-family:"Saira",sans-serif;font-weight:500;font-size:15px;line-height:24px;
    text-align:center;white-space:nowrap;
  }
  .label--cavoni .quality-band{background:var(--orange-band);color:var(--ink)}
  .label--ginger .quality-band{background:var(--green-band);color:#fff}
  .label--raspberry .quality-band{background:var(--red-band);color:#fff}
  .flavour{position:absolute;left:0;width:100%;text-align:center}
  .flavour--cavoni{top:325px;font-family:"Oswald",sans-serif;font-size:38px;color:var(--orange)}
  .flavour--ginger{top:340px;font-family:"Michroma",sans-serif;font-size:22px;line-height:28px;color:var(--green)}
  .flavour--raspberry{top:340px;font-family:"Montserrat",sans-serif;font-size:14px;letter-spacing:1px;color:var(--red)}
  .tagline{
    position:absolute;left:0;width:100%;text-align:center;
    font-family:"Pinyon Script",cursive;color:var(--ink);
  }
  .label--cavoni .tagline{top:390px;font-size:30px}
  .label--ginger .tagline{top:420px;font-size:24px}
  .label--raspberry .tagline{top:400px;font-size:24px}
  .fruit{position:absolute}
  .label--cavoni .fruit{left:110px;top:450px;width:150px;height:130px;border-radius:50%;background:radial-gradient(circle at 55% 60%,#f6a623 0%,#e9861a 55%,#25402a 100%)}
  .label--ginger .fruit{left:160px;top:450px;width:140px;height:150px;border-radius:40% 0 0 40%;background:radial-gradient(circle at 70% 45%,#b7dd5a 0%,#4fae5e 55%,#2f7d45 100%)}
  .label--raspberry .fruit{left:140px;top:470px;width:160px;height:120px;border-radius:45%;background:radial-gradient(circle at 40% 60%,#e12a35 0%,#b3121f 60%,#5fa033 100%)}
  .mint-leaf{position:absolute;left:118px;top:290px;width:64px;height:40px;border-radius:50%;background:linear-gradient(135deg,#6cb04a,#2f6b2a)}
  .volume{
    position:absolute;left:14px;top:520px;font-family:"Saira",sans-serif;color:var(--ink);line-height:1.15;
  }
  .label--cavoni .volume{font-size:20px}
  .label--ginger .volume,.label--raspberry .volume{top:538px;font-size:14px}
  .label__base{position:absolute;left:0;bottom:0;width:100%;height:70px}
</style>
</head>
<body>
<main class="range">

  <section class="label label--cavoni">
    <div class="label__cap"></div>
    <div class="brand">Velluta</div>
    <div class="quality-band">Genuine High Quality European Wine</div>
    <h2 class="flavour flavour--cavoni">Cavoni Spritz</h2>
    <p class="tagline">Natural Flavours</p>
    <div class="fruit" role="img" aria-label="Illustration of a halved orange with a dark green leaf"></div>
    <p class="volume">355 ml<br>5% alc./vol.</p>
    <svg class="label__base" viewBox="0 0 300 70" preserveAspectRatio="none" aria-hidden="true">
      <path d="M0 40 Q150 10 300 22 L300 70 L0 70 Z" fill="var(--orange-band)"/>
    </svg>
  </section>

  <section class="label label--ginger">
    <div class="label__cap"></div>
    <div class="brand">Velluta</div>
    <div class="quality-band">Genuine High Quality European Wine</div>
    <div class="mint-leaf" role="img" aria-label="Illustration of mint leaves"></div>
    <h2 class="flavour flavour--ginger">GINGER<br>LIME SPRITZ</h2>
    <p class="tagline">Natural Flavours</p>
    <div class="fruit" role="img" aria-label="Illustration of lime slices in a green liquid splash"></div>
    <p class="volume">355 ml<br>5% alc./vol.</p>
    <svg class="label__base" viewBox="0 0 300 70" preserveAspectRatio="none" aria-hidden="true">
      <path d="M0 40 Q150 10 300 22 L300 70 L0 70 Z" fill="var(--green-deep)"/>
    </svg>
  </section>

  <section class="label label--raspberry">
    <div class="label__cap"></div>
    <div class="brand">Velluta</div>
    <div class="quality-band">Genuine High Quality European Wine</div>
    <h2 class="flavour flavour--raspberry">RASPEBERRY-MIMOSA</h2>
    <p class="tagline">Natural Flavours</p>
    <div class="fruit" role="img" aria-label="Illustration of a cherry with leaf and a raspberry"></div>
    <p class="volume">355 ml<br>5% alc./vol.</p>
    <svg class="label__base" viewBox="0 0 300 70" preserveAspectRatio="none" aria-hidden="true">
      <path d="M0 40 Q150 10 300 22 L300 70 L0 70 Z" fill="var(--maroon)"/>
    </svg>
  </section>

</main>
</body>
</html>
```